DMVN Website

Hi we require a website with similar attributes and design to this http://style5.tarnbridgepages.com but obviously with all our information and images etc... also attached are our logos please do the design with the yellow logo not the red.

```html
<!DOCTYPE html>
<html lang="en">
<head>
<meta charset="utf-8">
<title>DMVN Collision Repair Centre</title>
<link href="https://fonts.googleapis.com/css2?family=Poppins:ital,wght@0,400;0,500;0,600;1,400&family=Oswald:wght@400;500&display=swap" rel="stylesheet">
<style>
:root{
  --yellow:#f2cc00;
  --dark:#333132;
  --ink:#222222;
  --text:#444444;
  --muted:#888888;
  --blue:#1f7fc4;
  --line:#e2e2e2;
  --white:#ffffff;
}
*{box-sizing:border-box;margin:0;padding:0}
html,body{width:1200px;height:3180px;overflow:hidden;background:var(--white)}
body{font-family:'Poppins',sans-serif;color:var(--text)}
.page{position:relative;width:1200px;height:3180px;overflow:hidden}
.abs{position:absolute}

/* header */
.site-header{position:absolute;left:0;top:0;width:1200px;height:92px;background:var(--white)}
.brand{position:absolute;left:86px;top:16px;display:flex;align-items:center;gap:10px}
.brand-mark{width:22px;height:22px;background:var(--yellow)}
.brand-name{font-size:20px;font-weight:600;color:var(--ink);line-height:1.1}
.brand-name small{display:block;font-size:11px;font-weight:600;letter-spacing:1px}
.top-contact{position:absolute;right:86px;top:12px;font-size:15px;color:var(--blue);display:flex;gap:22px}
.main-nav{position:absolute;right:86px;top:50px;display:flex;gap:26px;font-size:15px;color:var(--ink)}

/* hero */
.hero{position:absolute;left:0;top:92px;width:1200px;height:548px;overflow:hidden}
.hero-photo{position:absolute;inset:0;background:linear-gradient(100deg,#2a2a2c 0%,#5a524c 38%,#8e7f73 65%,#6b5e55 100%)}
.hero-text{position:absolute;left:585px;top:208px;font-family:'Oswald',sans-serif;color:var(--white)}
.hero-text .kicker{font-size:28px;color:var(--yellow);font-weight:400;line-height:1}
.hero-text h1{font-size:50px;font-weight:500;line-height:1.1;text-shadow:0 2px 4px rgba(0,0,0,.3)}
.hero svg{position:absolute;left:0;bottom:0}

/* section labels */
.label{font-size:19px;color:var(--yellow);position:absolute}
.heading{font-size:35px;font-weight:600;color:var(--ink);position:absolute;line-height:1.2}
.center{left:0;width:1200px;text-align:center}

.btn{position:absolute;background:var(--yellow);color:var(--ink);font-size:15px;font-weight:500;border-radius:22px;display:flex;align-items:center;justify-content:center}

/* welcome */
.welcome-copy{position:absolute;left:86px;top:790px;width:510px;font-size:12.8px;line-height:21.5px;color:var(--text)}
.welcome-photo{position:absolute;left:615px;top:713px;width:498px;height:320px;background:linear-gradient(180deg,#9aa0a3 0%,#5b6164 45%,#2d3032 100%);clip-path:polygon(40px 0,100% 0,100% 100%,0 100%)}

/* services */
.service{position:absolute;top:1195px;width:325px;text-align:center}
.service-photo{width:325px;height:305px}
.service h3{font-size:21px;font-weight:500;color:var(--ink);margin-top:16px}
.service p{font-size:12.5px;line-height:1.7;margin:14px 6px 0}
.dots{position:absolute;top:1730px;left:548px;display:flex;gap:8px}
.dots span{width:30px;height:3px;background:var(--dark)}
.dots span.on{background:var(--blue)}

/* appointment */
.appointment{position:absolute;left:0;top:1803px;width:607px;height:470px;background:var(--dark)}
.appointment-art{position:absolute;left:607px;top:1803px;width:593px;height:470px;background:var(--yellow)}
.appointment h2{position:absolute;left:86px;top:30px;font-size:28px;font-weight:600;color:var(--white)}
.field{position:absolute;background:var(--white);font-size:12.5px;color:var(--muted);padding:14px 12px;height:44px}

/* testimonial */
.quote-photo{position:absolute;left:95px;top:2447px;width:210px;height:238px;background:linear-gradient(160deg,#c7c9c4,#8b7b6c 60%,#6a5d52)}
.t-name{position:absolute;left:375px;top:2455px;font-size:20px;color:var(--blue)}
.t-role{position:absolute;left:375px;top:2485px;font-size:13px;color:var(--muted)}
.t-text{position:absolute;left:375px;top:2515px;width:745px;font-size:13.5px;line-height:21px;font-style:italic;color:var(--muted)}

/* gallery */
.gallery-pair{position:absolute;top:2860px;width:325px;height:122px;display:flex;gap:3px}
.gallery-pair div{flex:1}

/* footer */
.site-footer{position:absolute;left:0;top:3128px;width:1200px;height:52px;background:var(--dark)}
.social{position:absolute;left:86px;top:19px;display:flex;gap:14px}
.social span{width:14px;height:14px;border-radius:50%;background:var(--white)}
.legal{position:absolute;right:86px;top:16px;font-size:13px;color:#bbbbbb}
</style>
</head>
<body>
<div class="page">

<header class="site-header">
  <div class="brand"><span class="brand-mark"></span><span class="brand-name">DMVN<small>COLLISION REPAIR CENTRE</small></span></div>
  <div class="top-contact">
    <span>&#9993; info@dmvnrepair.com</span>
    <span>&#9742; (866) 555-0142</span>
  </div>
  <nav class="main-nav">
    <span>Home</span><span>Online Estimate Request</span><span>Services</span><span>Repair Status Update</span><span>Before and After</span><span>Testimonials</span><span>Contact Us</span>
  </nav>
</header>

<section class="hero">
  <div class="hero-photo" role="img" aria-label="Matte black sports car with red wheels on a warm brown backdrop"></div>
  <div class="hero-text">
    <div class="kicker">HIGHLY TRAINED</div>
    <h1>AUTO BODY TECHNICIANS</h1>
  </div>
  <svg width="1200" height="140" viewBox="0 0 1200 140">
    <path d="M0 110 C300 130 700 110 1200 30 L1200 140 L0 140 Z" fill="#ffffff"/>
    <path d="M0 100 C300 124 700 104 1200 22" fill="none" stroke="#1f6fb8" stroke-width="10"/>
    <path d="M0 112 C300 132 700 112 1200 34" fill="none" stroke="#3b9be0" stroke-width="3"/>
  </svg>
</section>

<section>
  <div class="label" style="left:86px;top:708px">Welcome</div>
  <h2 class="heading" style="left:86px;top:730px">Who we are?</h2>
  <p class="welcome-copy">We're excited to launch our new website! Please feel free to leave comments and suggestions. We are continually striving to improve our service and we welcome your input. At DMVN, we make customer service a priority. Our people are highly trained and are dedicated to the commitment of quality, workmanship and service that our business was in fact, founded on.<br>Our technicians have several years of experience behind them. We're proud to serve the auto body repair needs of the Dallas area. When the safety of your family is on the line, why settle for second best.</p>
  <div class="btn" style="left:86px;top:1012px;width:210px;height:40px">Online Estimate Request</div>
  <div class="welcome-photo" role="img" aria-label="Black coupe parked on a grey road"></div>
</section>

<section>
  <div class="label center" style="top:1106px">Services</div>
  <h2 class="heading center" style="top:1130px">What we offer</h2>
  <article class="service" style="left:86px">
    <div class="service-photo" role="img" aria-label="Technician spray painting a masked car rear" style="background:linear-gradient(160deg,#d9d9d9,#a9a9a9 60%,#5b6c80)"></div>
    <h3>Auto Body Repair</h3>
    <p>Sed ut perspiciatis unde omnis iste nat us error sit voluptatem Sed ut perspiciatis unde omnis iste nat us error sit voluptatem</p>
  </article>
  <article class="service" style="left:437px">
    <div class="service-photo" role="img" aria-label="Hands polishing a dark car panel" style="background:linear-gradient(160deg,#3c4a5c,#5d6a78 55%,#c9a26a)"></div>
    <h3>Paintless Dent Repair</h3>
    <p>Sed ut perspiciatis unde omnis iste nat us error sit voluptatem Sed ut perspiciatis unde omnis iste nat us error sit voluptatem</p>
  </article>
  <article class="service" style="left:789px">
    <div class="service-photo" role="img" aria-label="Gloved hand sanding a white car body" style="background:linear-gradient(160deg,#ecebe8,#d8d6d2 60%,#e3a25a)"></div>
    <h3>Auto Body Refinishing</h3>
    <p>Sed ut perspiciatis unde omnis iste nat us error sit voluptatem Sed ut perspiciatis unde omnis iste nat us error sit voluptatem</p>
  </article>
  <div class="btn" style="left:191px;top:1646px;width:115px;height:40px">Learn More</div>
  <div class="btn" style="left:542px;top:1646px;width:115px;height:40px">Learn More</div>
  <div class="btn" style="left:893px;top:1646px;width:115px;height:40px">Learn More</div>
  <div class="dots"><span></span><span class="on"></span><span></span></div>
</section>

<section class="appointment">
  <h2>Schedule an Appointment</h2>
  <div class="field" style="left:86px;top:90px;width:222px">Your Name</div>
  <div class="field" style="left:327px;top:90px;width:223px">Vehicle Number</div>
  <div class="field" style="left:86px;top:152px;width:222px">dd / mm / yyyy</div>
  <div class="field" style="left:327px;top:152px;width:223px">Select Time</div>
  <div class="field" style="left:86px;top:214px;width:464px">Select Service</div>
  <div class="field" style="left:86px;top:275px;width:464px;height:89px">Additional Notes</div>
  <div class="btn" style="left:86px;top:397px;width:127px;height:38px">Submit Now</div>
</section>
<div class="appointment-art" role="img" aria-label="Black silhouette of a sports car on yellow"></div>

<section>
  <div class="label center" style="top:2345px">Testimonial</div>
  <h2 class="heading center" style="top:2370px">What Peolpe are Saying</h2>
  <div class="abs" style="left:85px;top:2622px;width:72px;height:72px;background:var(--yellow)"></div>
  <div class="abs" style="left:245px;top:2440px;width:78px;height:78px;background:var(--dark)"></div>
  <div class="quote-photo" role="img" aria-label="Portrait of a smiling customer"></div>
  <div class="t-name">Jenna Moore</div>
  <div class="t-role">Customer for 3 years</div>
  <p class="t-text"><b style="color:var(--blue)">&ldquo;</b> Sed ut perspiciatis unde omnis iste natus error sit voluptatem accusantium doloremque laudantium, totam rem aperiam, eaque ipsa quae ab illo inventore veritatis et quasi architecto beatae vitae dicta sunt explicabo. Nemo enim ipsam voluptatem quia voluptas sit aspernatur aut odit aut fugit, sed quia consequuntur magni dolores eos qui ratione voluptatem sequi nesciunt. Neque porro quisquam est, qui dolorem ipsum quia dolor sit amet, consectetur, adipisci velit, sed quia non numquam eius modi tempora <b style="color:var(--blue)">&rdquo;</b></p>
  <svg class="abs" style="left:375px;top:2662px" width="50" height="20" viewBox="0 0 50 20">
    <path d="M10 4 L4 10 L10 16 M4 10 H16" stroke="#1f7fc4" stroke-width="2.5" fill="none"/>
    <path d="M22 16 L26 4" stroke="#999" stroke-width="1.5"/>
    <path d="M40 4 L46 10 L40 16 M46 10 H34" stroke="#1f7fc4" stroke-width="2.5" fill="none"/>
  </svg>
</section>

<section>
  <div class="label center" style="top:2765px">Our Gallery</div>
  <h2 class="heading center" style="top:2790px">Before &amp; After Pictures</h2>
  <div class="gallery-pair" style="left:86px">
    <div role="img" aria-label="Rusty classic car before restoration" style="background:linear-gradient(150deg,#6e7a62,#a0846a)"></div>
    <div role="img" aria-label="Restored classic car headlight" style="background:linear-gradient(150deg,#5a8f86,#c9c0b2)"></div>
  </div>
  <div class="gallery-pair" style="left:437px">
    <div role="img" aria-label="Old car in a field before repair" style="background:linear-gradient(150deg,#c9b9a2,#7a5a45)"></div>
    <div role="img" aria-label="Restored red classic car grille" style="background:linear-gradient(150deg,#b8312e,#d9d5d0)"></div>
  </div>
  <div class="gallery-pair" style="left:789px">
    <div role="img" aria-label="Classic car headlight before restoration" style="background:linear-gradient(150deg,#2b2b2b,#9a9a9a)"></div>
    <div role="img" aria-label="Restored teal car with red tail lights" style="background:linear-gradient(150deg,#6fb8b2,#c0392b)"></div>
  </div>
  <div class="btn" style="left:543px;top:3018px;width:115px;height:40px">View All</div>
</section>

<footer class="site-footer">
  <div class="social"><span></span><span></span><span></span></div>
  <div class="legal">&copy; 2018 All Rights Reserved. Terms of Use and Privacy Policy</div>
</footer>

</div>
</body>
</html>
```